Duel Business card

Want an edgy business card that shows both of our companies on each side of the card, OR both together with a cool design.

*Must be edgy: We have attached our two business logos. We are a bail bond and immigration bond company.

Would like the address on one side only.
Need Phone, cell, website, address, and Name

Company Name 1: Liberty Release Partners
www.libertyreleasepartners-example.com

Company Name 2: Crossway Custody Advocates
www.crosswaycustodyadvocates-example.com

These cards will need to be easily changeable so I can modify new employees

Target Market(s)

people in jail, takign imigrants out of jail and from being taken back to there country

Industry/Entity Type

Business

Requirements
Must have
• Include both logos attached

```html
<!DOCTYPE html>
<html lang="en">
<head>
<meta charset="utf-8">
<title>Liberty Release Partners / Crossway Custody Advocates – Business Cards</title>
<link href="https://fonts.googleapis.com/css2?family=Roboto:wght@400;500;700&display=swap" rel="stylesheet">
<style>
  :root {
    --navy: #1a2d87;
    --gold: #e3b527;
    --red: #e8222b;
    --white: #ffffff;
    --ink: #1d1d1f;
    --muted: #3a3a3a;
    --backdrop: #e6e6e6;
  }
  * { box-sizing: border-box; margin: 0; padding: 0; }
  html, body { width: 1200px; height: 900px; overflow: hidden; }
  body {
    background: var(--backdrop);
    font-family: "Roboto", Arial, sans-serif;
    position: relative;
  }
  .card {
    position: absolute;
    width: 510px;
    height: 310px;
    border-radius: 18px;
    overflow: hidden;
  }
  .card--front { background: var(--white); }
  .card--back { background: var(--navy); }
  .row-1 { top: 113px; }
  .row-2 { top: 471px; }
  .col-front { left: 65px; }
  .col-back { left: 626px; }

  /* front side */
  .brand-panel {
    position: absolute;
    left: 0; top: 0;
    width: 218px; height: 100%;
    background: var(--navy);
  }
  .brand-mark {
    position: absolute;
    left: 0; width: 100%;
    display: flex; flex-direction: column; align-items: center;
    text-align: center;
  }
  .brand-mark--primary { top: 28px; }
  .brand-mark--secondary { top: 172px; }
  .brand-dot {
    width: 52px; height: 52px;
    border-radius: 50%;
    background: var(--gold);
    margin-bottom: 10px;
  }
  .brand-mark--secondary .brand-dot { background: var(--white); width: 70px; height: 70px; }
  .brand-name {
    color: var(--white);
    font-weight: 700;
    font-size: 17px;
    line-height: 1.15;
    width: 180px;
  }
  .brand-mark--secondary .brand-name { font-size: 13px; }

  .contact-block {
    position: absolute;
    left: 275px; top: 0;
    width: 226px; height: 100%;
  }
  .person-name {
    position: absolute; top: 46px; left: 0;
    font-size: 16px; font-weight: 500; color: var(--ink);
  }
  .person-role {
    position: absolute; top: 69px; left: 0;
    font-size: 11px; color: var(--muted);
  }
  .contact-list {
    position: absolute; top: 172px; left: 0;
    list-style: none;
  }
  .contact-list li {
    display: flex; align-items: baseline;
    height: 21.5px;
    font-size: 10.5px; color: var(--muted);
    white-space: nowrap;
  }
  .contact-list .label {
    width: 16px; color: var(--navy); font-weight: 700; font-size: 11px;
  }
  .contact-list .small { font-size: 9.3px; }
  .accent-bar {
    position: absolute;
    left: 499px; top: 169px;
    width: 11px; height: 111px;
    background: var(--red);
  }

  /* back side */
  .back-mark {
    position: absolute; left: 0; width: 100%;
    display: flex; flex-direction: column; align-items: center;
    text-align: center;
  }
  .back-mark .brand-dot { width: 84px; height: 84px; margin-bottom: 16px; }
  .back-mark .brand-name { font-size: 30px; width: 420px; }
  .back-mark--primary { top: 64px; }
  .back-mark--secondary { top: 60px; }
  .back-mark--secondary .brand-dot { background: var(--white); width: 150px; height: 150px; margin-bottom: 12px; }
  .back-mark--secondary .brand-name { font-size: 22px; }
  .back-url {
    position: absolute; left: 0; width: 100%;
    text-align: center;
    color: var(--white);
    font-size: 19px; font-weight: 500;
  }
  .back-url--primary { top: 257px; }
  .back-url--secondary { top: 260px; font-size: 17px; font-weight: 400; }
</style>
</head>
<body>

  <!-- Front, version A -->
  <section class="card card--front row-1 col-front">
    <div class="brand-panel">
      <div class="brand-mark brand-mark--primary">
        <span class="brand-dot"></span>
        <span class="brand-name">Liberty Release Partners</span>
      </div>
      <div class="brand-mark brand-mark--secondary">
        <span class="brand-dot"></span>
        <span class="brand-name">Crossway Custody Advocates</span>
      </div>
    </div>
    <div class="contact-block">
      <p class="person-name">Daniel Marlow</p>
      <p class="person-role">Manager</p>
      <ul class="contact-list">
        <li><span class="label">P</span>1-888-555-0142</li>
        <li><span class="label">P</span>1-877-555-0178</li>
        <li><span class="label">M</span><span class="small">dmarlow@libertyreleasepartners-example.com</span></li>
        <li><span class="label">W</span><span class="small">www.libertyreleasepartners-example.com</span></li>
        <li><span class="label">W</span><span class="small">www.crosswaycustodyadvocates-example.com</span></li>
      </ul>
    </div>
    <span class="accent-bar"></span>
  </section>

  <!-- Back, version A -->
  <section class="card card--back row-1 col-back">
    <div class="back-mark back-mark--primary">
      <span class="brand-dot"></span>
      <span class="brand-name">Liberty Release Partners</span>
    </div>
    <p class="back-url back-url--primary">www.libertyreleasepartners-example.com</p>
  </section>

  <!-- Front, version B -->
  <section class="card card--front row-2 col-front">
    <div class="brand-panel">
      <div class="brand-mark brand-mark--primary">
        <span class="brand-dot"></span>
        <span class="brand-name">Liberty Release Partners</span>
      </div>
      <div class="brand-mark brand-mark--secondary">
        <span class="brand-dot"></span>
        <span class="brand-name">Crossway Custody Advocates</span>
      </div>
    </div>
    <div class="contact-block">
      <p class="person-name">Daniel Marlow</p>
      <p class="person-role">Manager</p>
      <ul class="contact-list">
        <li><span class="label">P</span>1-888-555-0142</li>
        <li><span class="label">P</span>1-877-555-0178</li>
        <li><span class="label">M</span><span class="small">dmarlow@libertyreleasepartners-example.com</span></li>
        <li><span class="label">W</span><span class="small">www.libertyreleasepartners-example.com</span></li>
        <li><span class="label">W</span><span class="small">www.crosswaycustodyadvocates-example.com</span></li>
      </ul>
    </div>
    <span class="accent-bar"></span>
  </section>

  <!-- Back, version B -->
  <section class="card card--back row-2 col-back">
    <div class="back-mark back-mark--secondary">
      <span class="brand-dot"></span>
      <span class="brand-name">Crossway Custody Advocates</span>
    </div>
    <p class="back-url back-url--secondary">www.crosswaycustodyadvocates-example.com</p>
  </section>

</body>
</html>
```